Designing HTML Email Creative

Hi There,
The goal of this project is to design an HTML Email Creative.
Target Market: Minority Women 25 - 45. Low Household incomes. Stay at home moms. Middle America
Subject of Email Campaign: Top 5 Reasons To Go Back to College
The goal is to make the users Buy the top 5 reasons to go back to school and then Get Matched to Online & Local Colleges.
Call to action: Get Matched to Online & Local Colleges
You can add two buttons, one above the reasons and one below. The text in the button should be: Get Matched to Online & Local Colleges Now!
Your goal is to make the call to action in the email pop out so that users know very easily where to click to visit our site.
Please find attached the copy that is to be used in the creative.
Also, the information needs to be sourced so you can create very small links in the bottom of the email.
Also, we just need the psd file for this. Does not need to be coded.
Also, you can find some successful email creative attached so you have an idea.
Updates
Please note that we have updated the word doc with the correct content.
Target Market(s)
Women 25 - 50 - Low Household Incomes - Middle America
Industry/Entity Type
School
Look and feel

```html
<!DOCTYPE html>
<html lang="en">
<head>
<meta charset="utf-8">
<title>Top 5 Reasons to Go Back to College</title>
<link href="https://fonts.googleapis.com/css2?family=Open+Sans:wght@300;400;600&family=Roboto+Condensed:wght@400;700&display=swap" rel="stylesheet">
<style>
  :root {
    --crimson: #d3224f;
    --crimson-deep: #9c0e2c;
    --pink-bg: #fbd7e2;
    --pink-light: #fde6ee;
    --badge: #f0507a;
    --ink: #222222;
    --ink-soft: #333333;
    --highlight-dark: #b51c3f;
    --edge-band: #f3b9ca;
    --white: #ffffff;
  }
  * { margin: 0; padding: 0; box-sizing: border-box; }
  html, body { width: 686px; height: 1200px; overflow: hidden; }
  body { background: var(--white); font-family: "Open Sans", Arial, sans-serif; }

  .email {
    position: relative;
    width: 686px;
    height: 1200px;
    background: radial-gradient(ellipse at 50% 40%, var(--pink-light), var(--pink-bg) 75%);
    overflow: hidden;
  }

  .hero {
    position: absolute; left: 0; top: 0;
    width: 686px; height: 258px;
    background: linear-gradient(135deg, #8a4a3a 0%, #c23a4e 40%, #d42a50 65%, #c41d48 100%);
  }
  .hero-title {
    position: absolute; left: 0; top: 194px;
    width: 686px; text-align: center;
    font-family: "Roboto Condensed", "Arial Narrow", sans-serif;
    font-weight: 400; font-size: 44px; letter-spacing: -0.6px;
    color: var(--white);
    text-shadow: 0 0 3px var(--crimson-deep), 2px 2px 3px var(--crimson-deep), -2px -1px 3px var(--crimson-deep);
  }

  .intro {
    position: absolute; left: 0; top: 283px; width: 686px;
    text-align: center; color: var(--crimson);
    font-size: 18.5px; line-height: 31px;
  }
  .intro .mark {
    color: var(--white); background: var(--crimson); padding: 1px 3px;
  }
  .intro .mark-dark { background: var(--highlight-dark); box-shadow: inset 0 0 0 1px #7d0d25; }

  .cta {
    position: absolute; left: 55px; width: 567px; height: 48px;
    border-radius: 24px;
    background: linear-gradient(to bottom, #f86b8a 0%, #e8335a 45%, #c9143e 55%, #b5102f 100%);
    box-shadow: 0 2px 3px rgba(120, 10, 40, 0.45);
    color: var(--white); text-decoration: none;
    font-family: "Roboto Condensed", "Arial Narrow", sans-serif;
    font-weight: 700; font-size: 23.5px;
    display: flex; align-items: center; justify-content: center;
    text-shadow: 0 1px 1px rgba(90, 0, 20, 0.5);
  }
  .cta-top { top: 416px; }
  .cta-bottom { top: 1119px; }

  .reason { position: absolute; left: 46px; width: 602px; }
  .reason-number {
    position: absolute; left: 0; top: 0;
    width: 29px; height: 29px; border-radius: 50%;
    background: var(--badge); color: var(--white);
    font-size: 17px; line-height: 29px; text-align: center;
  }
  .reason-title {
    margin-left: 42px; font-size: 16.5px; font-weight: 600;
    color: var(--ink); line-height: 29px;
  }
  .reason-body {
    margin-left: 42px; margin-top: 2px;
    font-size: 16px; line-height: 24px; color: var(--ink-soft);
    text-align: justify;
  }
  .reason-1 { top: 486px; }
  .reason-2 { top: 623px; }
  .reason-3 { top: 784px; }
  .reason-4 { top: 897px; }
  .reason-5 { top: 1010px; }
  .reason-5 .reason-title { font-weight: 400; }
  .reason-5 .reason-body { font-size: 15.5px; font-weight: 300; color: var(--ink); }

  .edge-band {
    position: absolute; left: 0; top: 1186px;
    width: 686px; height: 14px;
    background: linear-gradient(to bottom, var(--pink-bg), var(--edge-band));
  }
</style>
</head>
<body>
<div class="email">
  <div class="hero" role="img" aria-label="Photo of a smiling young woman holding a book"></div>
  <h1 class="hero-title">Top 5 Reasons to Go Back to College</h1>

  <p class="intro">
    Empower <span class="mark">yourself!</span><br>
    Education frees you financially and<br>
    boosts your <span class="mark mark-dark">self-esteem</span> and self-confidence.
  </p>

  <a class="cta cta-top" href="#">Get Matched to Online &amp; Local Colleges Now</a>

  <section class="reason reason-1">
    <span class="reason-number">1</span>
    <h2 class="reason-title">Education Pays – Make Double the Money.</h2>
    <p class="reason-body">College grads earn nearly twice as much as those with only high school diplomas. Median weekly salary with high school diploma, $652. Median weekly salary with Bachelor’s degree $1,066.</p>
  </section>

  <section class="reason reason-2">
    <span class="reason-number">2</span>
    <h2 class="reason-title">Government Grants – Federal Pell Grants</h2>
    <p class="reason-body">College is more affordable than you think. Federal Pell Grants of up to $5,550 are available to qualifying students. Grants are free money, which does not have to be paid back. Other Federal and state grants are also available, as are low cost government loans and countless scholarships.</p>
  </section>

  <section class="reason reason-3">
    <span class="reason-number">3</span>
    <h2 class="reason-title">Lower Unemployment Rates for College Grads.</h2>
    <p class="reason-body">High school graduates 8.3% unemployed, college graduates 4.5% unemployed.</p>
  </section>

  <section class="reason reason-4">
    <span class="reason-number">4</span>
    <h2 class="reason-title">Make $1 Million More in Lifetime – Retirement Security</h2>
    <p class="reason-body">On average, those with a bachelor’s degree earn a $1 million more in their lifetime than those with a high school diploma.</p>
  </section>

  <section class="reason reason-5">
    <span class="reason-number">5</span>
    <h2 class="reason-title">Be More Employable</h2>
    <p class="reason-body">Of the 2 million plus job added during the recent U.S. economic recovery, the majorities were for college graduates.</p>
  </section>

  <a class="cta cta-bottom" href="#">Get Matched to Online &amp; Local Colleges Now</a>

  <div class="edge-band" role="img" aria-label="Decorative border along the bottom edge"></div>
</div>
</body>
</html>
```